financial company web page

We are tax and financial consulting company that needs a web site. Our logo is attached. Headquarters of our company is based in Latvia, Riga. Our actual temporary web site is www.corvanteq.com The main purpose of our new web site is:
* to explain the benefits of doing business through Latvian LLC companies;
* provide necessary information about taxation regime in Latvia for trading and holding companies
* propose some standard schemes of using Latvian companies for various businesses.
* offer our clients other jurisdictions companies - other European, offshore, etc.
* offer our clients ecommerce solutions
* offer our client residency in Latvia and EU
Registration of a Latvian company + accounting + legal advice will be our primary product. However, web site first page should highlight 4 other important products, such as:
1 - eCommerce (here we will explain briefly what is eCommerce, how our client can use it, what are the bonuses doing business online, explain conditions of eCommerce, etc) ;
2 - Residence Permit (here we offer EU and non-EU citizens to obtain Latvian residence permit and explain the benefits of having Latvian ID card);
3 - other Jurisdictions (here we propose list of other companies registered in the countries with favorable taxation regime, i.e. UK, Hong-Kong, Canada, Panama, BVI, UAE, etc);
4 - banking (here we explain benefits of having bank account in Latvia, explaining briefly products that bank offer, etc).
Overall Website map is the following:
1. About us
2. About Latvia
3. Contacts
4. Latvian company
5. Our services
a. еCommerce
b. Resident permit (Latvia and EU)
c. Bank accounts
d. Registration and support of other jurisdictions (European companies, Low tax companies, Offshore companies)
e. Additional services (Tax advisory, Virtual office, European licenses, Accounting services, Legal address in Riga)
6. Become Partner
7. Corvanteq Travel Guide
As a start point we need only first page design. If this design suits us well we will continue to work with you on other pages. We are looking for innovative, creative and professional design in line with our corporate logo and colours. We want this design to focus more on graphic, on simplicity and usability. It should be immediately clear from the first glance what the site is about, what is our key product and how to get more information if I'm interested on something.
These are website from our sector, we want to be better:
http://www.marlowbayholdings.com/
http://www.qtr-harbourline.com/
http://www.dwpenterprisehub.com/
http://www.firmsetupnorth59.co.uk/
In case you can't find our logo, please, ask I will send it to your mail. Thanks!
Target Market(s)
European, Russian or Chinesee enterpreneurs
Industry/Entity Type
Accounting
Requirements
Must have
- Web site will be on 10 languages, so somewhere must be a button/flag to switch language.
Contact information should be on every page (phone number and add Chatterloop buttons or similar).
Search button should be available on the first page
Button Request a Call should be on every page.
Visitors should also have a possibility to download a brochure about each product (so appropriate button should be in each section).

```html
<!DOCTYPE html>
<html lang="en">
<head>
<meta charset="utf-8">
<title>Corvanteq — Tax and Financial Solutions</title>
<link rel="stylesheet" href="https://fonts.googleapis.com/css2?family=PT+Sans:wght@400;700&family=Arimo:wght@400;700&display=swap">
<style>
  :root {
    --brand-navy: #163f7c;
    --brand-blue: #1d4f93;
    --nav-top: #2a5ea3;
    --nav-bottom: #0f3b76;
    --nav-edge: #4a7fc0;
    --ink: #111111;
    --panel-bg: rgba(240, 240, 243, 0.94);
    --divider: #333333;
    --page-bg: #ffffff;
    --sky-top: #252c3c;
    --sky-mid: #3a4256;
    --city-low: #3b3140;
    --city-glow: #7a5a3c;
  }
  * { box-sizing: border-box; margin: 0; padding: 0; }
  html, body { width: 1200px; height: 1045px; overflow: hidden; background: var(--page-bg); }
  .page { position: relative; width: 1200px; height: 1045px; font-family: "Arimo", Arial, sans-serif; color: var(--ink); }

  .brand { position: absolute; left: 34px; top: 40px; display: flex; align-items: center; gap: 14px; }
  .brand-dot { width: 56px; height: 56px; border-radius: 50%; background: var(--brand-navy); }
  .brand-name { font-family: "PT Sans", sans-serif; font-weight: 700; font-size: 58px; color: var(--brand-navy); letter-spacing: 0.5px; }

  .languages { position: absolute; right: 14px; top: 8px; display: flex; gap: 7px; }
  .languages svg { display: block; }

  .search { position: absolute; left: 938px; top: 110px; width: 252px; height: 29px; display: flex; }
  .search-field { flex: 1; border: 1px solid var(--brand-navy); border-right: none; font-family: "PT Sans", sans-serif; font-size: 17px; color: var(--brand-navy); padding: 3px 8px; line-height: 21px; white-space: nowrap; overflow: hidden; }
  .search-button { width: 31px; background: var(--brand-navy); display: flex; align-items: center; justify-content: center; }

  .main-nav { position: absolute; left: 0; top: 149px; width: 1200px; height: 41px; display: flex;
    background: linear-gradient(var(--nav-top), var(--nav-bottom) 70%, var(--nav-edge) 72%, var(--nav-bottom)); }
  .main-nav a { display: flex; align-items: center; justify-content: center; color: #fff; text-decoration: none;
    font-family: "PT Sans", sans-serif; font-size: 20px; border-right: 2px solid #fff; }
  .main-nav a:last-child { border-right: none; }

  .hero-photo { position: absolute; left: 0; top: 198px; width: 1200px; height: 803px;
    background:
      radial-gradient(ellipse 60% 12% at 50% 58%, rgba(210,170,110,0.35), transparent 70%),
      linear-gradient(180deg, var(--sky-top) 0%, var(--sky-mid) 22%, #2e3648 36%, var(--city-glow) 50%, #3a4a6a 58%, var(--city-low) 80%, #2a2430 100%); }

  .products { position: absolute; left: 29px; top: 551px; width: 1143px; height: 391px; background: var(--panel-bg); display: flex; }
  .product { text-align: center; padding: 0 10px; border-right: 1px solid var(--divider); }
  .product:last-child { border-right: none; }
  .product-title { font-family: "PT Sans", sans-serif; font-weight: 400; font-size: 19px; color: var(--brand-navy); margin-top: 30px; }
  .product-lead { font-weight: 700; font-size: 14.6px; line-height: 19.3px; margin-top: 24px; }
  .product-body { font-size: 14.6px; line-height: 19.3px; margin-top: 19px; }

  .footer-nav { position: absolute; left: 16px; top: 1010px; display: flex; gap: 51px; }
  .footer-nav a { font-family: "PT Sans", sans-serif; font-size: 19px; color: var(--brand-navy); text-decoration: none; }
</style>
</head>
<body>
<div class="page">
  <header>
    <div class="brand">
      <span class="brand-dot"></span>
      <span class="brand-name">Corvanteq</span>
    </div>

    <nav class="languages" aria-label="Language">
      <svg width="27" height="27" role="img" aria-label="English"><circle cx="13.5" cy="13.5" r="12.5" fill="#2b3e8c"/><path d="M2 13.5h23M13.5 2v23" stroke="#d22" stroke-width="4"/></svg>
      <svg width="27" height="27" role="img" aria-label="French"><clipPath id="cf"><circle cx="13.5" cy="13.5" r="12.5"/></clipPath><g clip-path="url(#cf)"><rect width="9" height="27" fill="#1b3f9a"/><rect x="9" width="9" height="27" fill="#fff"/><rect x="18" width="9" height="27" fill="#d8232a"/></g></svg>
      <svg width="27" height="27" role="img" aria-label="German"><clipPath id="cd"><circle cx="13.5" cy="13.5" r="12.5"/></clipPath><g clip-path="url(#cd)"><rect width="27" height="9" fill="#111"/><rect y="9" width="27" height="9" fill="#d0101a"/><rect y="18" width="27" height="9" fill="#f5c400"/></g></svg>
      <svg width="27" height="27" role="img" aria-label="Chinese"><circle cx="13.5" cy="13.5" r="12.5" fill="#d0151a"/></svg>
      <svg width="27" height="27" role="img" aria-label="Spanish"><clipPath id="ce"><circle cx="13.5" cy="13.5" r="12.5"/></clipPath><g clip-path="url(#ce)"><rect width="27" height="27" fill="#c8141c"/><rect y="7" width="27" height="13" fill="#f6c400"/></g></svg>
      <svg width="27" height="27" role="img" aria-label="Japanese"><circle cx="13.5" cy="13.5" r="12.5" fill="#f2f2f2" stroke="#bbb"/><circle cx="13.5" cy="13.5" r="5.5" fill="#d0151a"/></svg>
      <svg width="27" height="27" role="img" aria-label="Portuguese"><clipPath id="cp"><circle cx="13.5" cy="13.5" r="12.5"/></clipPath><g clip-path="url(#cp)"><rect width="11" height="27" fill="#1a7a2a"/><rect x="11" width="16" height="27" fill="#d0151a"/></g></svg>
    </nav>

    <form class="search" role="search">
      <div class="search-field">Search..................................</div>
      <div class="search-button">
        <svg width="18" height="14" aria-hidden="true"><path d="M1 7h15M10 1.5l6 5.5-6 5.5" stroke="#fff" stroke-width="2" fill="none"/></svg>
      </div>
    </form>
  </header>

  <nav class="main-nav" aria-label="Main">
    <a href="#" style="width:239px">LATVIAN COMPANY</a>
    <a href="#" style="width:239px">OTHER JURIDICITIONS</a>
    <a href="#" style="width:242px">E-COMMERCE</a>
    <a href="#" style="width:240px">RESIDENCE PERMIT</a>
    <a href="#" style="width:240px">VIRTUAL OFFICE</a>
  </nav>

  <div class="hero-photo" role="img" aria-label="Night panorama of Riga with the river, an illuminated bridge and old town towers"></div>

  <main class="products">
    <section class="product" style="width:287px">
      <h2 class="product-title">PRODUCT 1</h2>
      <p class="product-lead">Lorem ipsum dolor sit amet, consec tetuer adipiscing elit. Praesent vestibulum molestie lacus. Aenean nonummy hen drerit mauris. Phasellus porta. Fusce suscipit varius mi.</p>
      <p class="product-body">Cum sociis natoque penatibus et magnis dis parturient montes, nascetur ridiculus mus. Nulla dui. Fusce feugiat malesuada odio. Morbi nunc odio, gravida at, cursus nec, luctus a, lorem. Maecenas tristique orci ac sem. Duis ultricies pharetra magna. D Donec sit amet</p>
    </section>
    <section class="product" style="width:287px">
      <h2 class="product-title">PRODUCT 2</h2>
      <p class="product-lead">Lorem ipsum dolor sit amet, consec tetuer adipiscing elit. Praesent vestibulum molestie lacus. Aenean nonummy hen drerit mauris. Phasellus porta. Fusce suscipit varius mi.</p>
      <p class="product-body">Cum sociis natoque penatibus et magnis dis parturient montes, nascetur ridiculus mus. Nulla dui. Fusce feugiat malesuada odio. Morbi nunc odio, gravida at, cursus nec, luctus a, lorem. Maecenas tristique orci ac sem. Duis ultricies pharetra magna. D Donec sit amet</p>
    </section>
    <section class="product" style="width:299px">
      <h2 class="product-title">PRODUCT 3</h2>
      <p class="product-lead">Lorem ipsum dolor sit amet, consec tetuer adipiscing elit. Praesent vestibulum molestie lacus. Aenean nonummy hen drerit mauris. Phasellus porta. Fusce suscipit varius mi.</p>
      <p class="product-body">Cum sociis natoque penatibus et magnis dis parturient montes, nascetur ridiculus mus. Nulla dui. Fusce feugiat malesuada odio. Morbi nunc odio, gravida at, cursus nec, luctus a, lorem. Maecenas tristique orci ac sem. Duis ultricies pharetra magna. D Donec sit amet</p>
    </section>
    <section class="product" style="width:270px">
      <h2 class="product-title">PRODUCT 4</h2>
      <p class="product-lead">Lorem ipsum dolor sit amet, consec tetuer adipiscing elit. Praesent vestibulum molestie lacus. Aenean nonummy hen drerit mauris. Phasellus porta. Fusce suscipit varius mi.</p>
      <p class="product-body">Cum sociis natoque penatibus et magnis dis parturient montes, nascetur ridiculus mus. Nulla dui. Fusce feugiat malesuada odio. Morbi nunc odio, gravida at, cursus nec, luctus a, lorem. Maecenas tristique orci ac sem. Duis ultricies pharetra magna. D Donec sit amet</p>
    </section>
  </main>

  <footer class="footer-nav">
    <a href="#">Site MAP</a>
    <a href="#">Contacts</a>
    <a href="#">Legal</a>
  </footer>
</div>
</body>
</html>
```